ADVERT DESIGN FOR INTERNATIONAL PAYMENTS COMPANY

Looking to design an advert for our business. We specialise in selling FX and making international payments.
Advert should come across as professional and discreet
Points to note are,
Authorised by QTLB and the ZVP
Bank-Beating Exchange Rates
0% Commission
UK Office: 47 Ormbury Terrace London SE19 4QT
Gibraltar Office: Suite 5C Tavistone Court 8 Merrow Steps Gibraltar GX11 9ZZ
E: desk@pelvorex.co.uk
T: 020 81570394
There shouldn't be any other text. As a suggestion the background image should perhaps be reminiscent of our ability to make payments across the word quickly and securely. But other ideas welcome.

```html
<!DOCTYPE html>
<html lang="en">
<head>
<meta charset="utf-8">
<title>Pelvorex – International Payments Advert</title>
<link rel="stylesheet" href="https://fonts.googleapis.com/css2?family=Poppins:wght@200;300;400;600;700;800&display=swap">
<style>
  :root {
    --navy: #1a2d5c;
    --navy-deep: #152650;
    --teal: #1f8fa8;
    --teal-light: #3fb6c9;
    --white: #ffffff;
  }
  * { margin: 0; padding: 0; box-sizing: border-box; }
  html, body { width: 1200px; height: 1200px; overflow: hidden; }
  body {
    background: var(--navy);
    font-family: "Poppins", sans-serif;
    color: var(--white);
  }
  .advert {
    position: relative;
    width: 1200px;
    height: 1200px;
    overflow: hidden;
    background: radial-gradient(ellipse at 20% 10%, #24407a 0%, var(--navy) 45%, var(--navy-deep) 100%);
  }
  .network-backdrop {
    position: absolute;
    inset: 0;
    background:
      radial-gradient(circle at 1016px 1200px, rgba(63,182,201,0.0) 0, rgba(63,182,201,0.0) 560px, rgba(63,182,201,0.12) 600px, rgba(63,182,201,0) 700px);
  }
  .globe {
    position: absolute;
    left: 456px;
    top: 640px;
    width: 1120px;
    height: 1120px;
    border-radius: 50%;
    background: radial-gradient(circle at 45% 35%, var(--teal-light) 0%, var(--teal) 30%, #175f86 60%, #1a3c6e 85%);
    opacity: 0.9;
  }
  .rule {
    position: absolute;
    left: 97px;
    width: 1px;
    background: var(--white);
  }
  .rule--top { top: 0; height: 844px; }
  .rule--bottom { top: 1106px; height: 94px; }
  .headline-block {
    position: absolute;
    left: 202px;
    top: 182px;
  }
  .authorisation {
    font-weight: 300;
    font-size: 32px;
    letter-spacing: 0.3px;
  }
  .headline {
    margin-top: 26px;
    font-weight: 700;
    font-size: 80px;
    line-height: 0.8;
    letter-spacing: -1px;
    text-transform: uppercase;
  }
  .offer {
    margin-top: 58px;
    font-weight: 700;
    font-size: 80px;
    line-height: 0.8;
    letter-spacing: -1px;
  }
  .contacts {
    position: absolute;
    left: 83px;
    top: 864px;
    list-style: none;
  }
  .contact {
    display: flex;
    align-items: center;
    gap: 17px;
    margin-bottom: 14px;
  }
  .contact-icon { width: 28px; height: 28px; flex: none; }
  .contact-label { font-weight: 200; font-size: 21px; line-height: 1.1; }
  .contact-value { font-weight: 700; font-size: 21px; line-height: 1.3; }
  .contact--single { margin-bottom: 20px; }
  .brand {
    position: absolute;
    right: 106px;
    top: 1050px;
    font-weight: 600;
    font-size: 38px;
    color: var(--white);
  }
</style>
</head>
<body>
<main class="advert">
  <div class="network-backdrop" role="img" aria-label="Faint network of connected points across the dark blue sky"></div>
  <div class="globe" role="img" aria-label="Glowing teal globe with light connections spanning the continents"></div>

  <div class="rule rule--top"></div>
  <div class="rule rule--bottom"></div>

  <section class="headline-block">
    <p class="authorisation">Authorised by QTLB and the ZVP</p>
    <h1 class="headline">Bank-Beating<br>Exchange Rates</h1>
    <p class="offer">0% COMMISSION</p>
  </section>

  <ul class="contacts">
    <li class="contact">
      <svg class="contact-icon" viewBox="0 0 28 28" fill="none" stroke="#fff" stroke-width="1.2">
        <circle cx="14" cy="14" r="13"/>
        <path d="M14 20s-4-4.2-4-7a4 4 0 0 1 8 0c0 2.8-4 7-4 7z"/>
        <circle cx="14" cy="13" r="1.3"/>
      </svg>
      <div>
        <p class="contact-label">UK Office:</p>
        <p class="contact-value">47 Ormbury Terrace London SE19 4QT</p>
      </div>
    </li>
    <li class="contact">
      <svg class="contact-icon" viewBox="0 0 28 28" fill="none" stroke="#fff" stroke-width="1.2">
        <circle cx="14" cy="14" r="13"/>
        <path d="M14 20s-4-4.2-4-7a4 4 0 0 1 8 0c0 2.8-4 7-4 7z"/>
        <circle cx="14" cy="13" r="1.3"/>
      </svg>
      <div>
        <p class="contact-label">Gibraltar Office:</p>
        <p class="contact-value">Suite 5C Tavistone Court 8 Merrow Steps Gibraltar GX11 9ZZ</p>
      </div>
    </li>
    <li class="contact contact--single">
      <svg class="contact-icon" viewBox="0 0 28 28" fill="none" stroke="#fff" stroke-width="1.2">
        <circle cx="14" cy="14" r="13"/>
        <rect x="8.5" y="10" width="11" height="8" rx="1"/>
        <path d="M8.5 10.5l5.5 4 5.5-4"/>
      </svg>
      <p class="contact-value">desk@pelvorex.co.uk</p>
    </li>
    <li class="contact contact--single">
      <svg class="contact-icon" viewBox="0 0 28 28" fill="none" stroke="#fff" stroke-width="1.2">
        <circle cx="14" cy="14" r="13"/>
        <path d="M10 8.5l2.2 2.6-1.3 1.8c.8 1.7 2.1 3 3.8 3.8l1.8-1.3 2.6 2.2-1.4 1.9c-4.2-.3-8.3-4.4-8.6-8.6z"/>
      </svg>
      <p class="contact-value">020 81570394</p>
    </li>
  </ul>

  <p class="brand">Pelvorex</p>
</main>
</body>
</html>
```